Business Card for a finance professional

I need a business card design to introduce myself to a professional networking (mainly banks) and potential companies to hire and remember me. I would like to use black, grey, white and maybe gold/silver colors and maybe something with my initials(R L F P T). The final design should communicate seriousness, profissionalism and something innovative.

The basic informations in the card are: Name, e-mail, phone number and trabnet. (I'm thinking to put some directly short link to my trabnet account or maybe some app - non QR Code - to add my contacts to a phone directly.)

My name is Mariana Lopes Ferreira Pinto dos Reis (I prefer to use only 'Mariana Lopes' or 'Mariana Reis' but i'm open to other suggestions) and I have 26 years old (just if it helps to build based in my age).
Updates

Dear designers, I wish to thank your participation in this project! It was very difficult to choose one! Thank your for your work! Best regards and success. Mariana

Target Market(s)

Potential hires and big companies.

Industry/Entity Type

Finance

Requirements
Must have
• The informations required at the business card are:
Name: Mariana Lopes F. P. dos Reis
Email: mariana.lop.reis@quellomail.com
Phone: +55 61 8493 5710
TrabNet: http://br.trabnet-perfis.com/in/marianalr/
Nice to have
• Modern and innovative look.
I suggest to use the colors black, grey, white, gold and/or silver, but I'm open to other colors.
Should not have
• A message showing that I need to be hired. It's more to "know me and remember me" than "hire me please".

```html
<!DOCTYPE html>
<html lang="en">
<head>
<meta charset="utf-8">
<title>RLFPT Capital — Business Card</title>
<link rel="stylesheet" href="https://fonts.googleapis.com/css2?family=Open+Sans:wght@400;600&display=swap">
<style>
  :root {
    --backdrop: #7a6d6e;
    --card: #0d0b0c;
    --card-soft: #1a1819;
    --ink: #ffffff;
    --ink-muted: #e8e6e6;
    --accent: #d9534f;
  }
  * { box-sizing: border-box; margin: 0; padding: 0; }
  html, body {
    width: 1200px;
    height: 857px;
    overflow: hidden;
    background: var(--backdrop);
    font-family: "Open Sans", Arial, sans-serif;
  }
  .canvas {
    position: relative;
    width: 1200px;
    height: 857px;
    display: flex;
    align-items: center;
    justify-content: center;
    gap: 60px;
  }
  .card {
    position: relative;
    width: 510px;
    height: 292px;
    background: var(--card);
    color: var(--ink);
  }
  .card--back { background: var(--card-soft); }

  .card__name {
    position: absolute;
    top: 58px;
    left: 40px;
    right: 24px;
    font-size: 16px;
    font-weight: 400;
    letter-spacing: 0.2px;
    color: var(--ink-muted);
    white-space: nowrap;
  }
  .card__rule {
    position: absolute;
    top: 98px;
    left: 260px;
    width: 30px;
    height: 3px;
    background: var(--accent);
  }
  .card__contacts {
    position: absolute;
    left: 44px;
    top: 140px;
    list-style: none;
    font-size: 10px;
    line-height: 14px;
    color: var(--ink-muted);
  }

  .card--front {
    display: flex;
    align-items: center;
    justify-content: center;
    gap: 14px;
  }
  .brand__square {
    width: 22px;
    height: 22px;
    background: var(--ink);
  }
  .brand__name {
    font-size: 34px;
    font-weight: 600;
    letter-spacing: 1px;
    color: var(--ink);
    line-height: 1;
  }
</style>
</head>
<body>
  <main class="canvas">
    <section class="card card--back" aria-label="Card back with contact details">
      <p class="card__name">Mariana Lopes Ferreira Pinto dos Reis</p>
      <span class="card__rule"></span>
      <ul class="card__contacts">
        <li>+55 61 8493 5710</li>
        <li>mariana.lop.reis@quellomail.com</li>
        <li>http://br.trabnet-perfis.com/in/marianalr/</li>
      </ul>
    </section>

    <section class="card card--front" aria-label="Card front with company name">
      <span class="brand__square"></span>
      <span class="brand__name">RLFPT Capital</span>
    </section>
  </main>
</body>
</html>
```